Business Card Design Project

I need a business card design for my freelance solo makeup artistry business in Melbourne, Australia called Rosa Marindi. My freelance business specialises in bridal and special occassions makeup.

I like the idea of having Rosa Marindi in pink as its a feminine and soft colour. I would like a very clean, classy and simple (with an element of fun if that's possible) design. I would consider the business name to be in gloss with an otherwise matte finish.

Underneath the business name, I would like "Makeup by Tessa Colwick"

I do not want any bridal related graphics.

Target Market(s)

Young females with a disposable income from ages 20-40 and females getting married who will dictate who does mother of bride makeup ages 40-70.

Industry/Entity Type

Business

Requirements
Must have
• "Makeup by Tessa Colwick"

Ph: 0412 385 604
E: rosamarindi@inboxly.net
ABN: 58204917362
Nice to have
• I think I would like a mini business cards which is more slimline. I do like the colours of pink, white and grey but open to suggestions.
Should not have
• Bridal related graphics

```html
<!DOCTYPE html>
<html lang="en">
<head>
<meta charset="utf-8">
<title>Rosa Marindi – Business Card</title>
<link rel="stylesheet" href="https://fonts.googleapis.com/css2?family=Arimo:ital@0;1&family=Pinyon+Script&display=swap">
<style>
  :root {
    --paper: #ffffff;
    --pink: #f6c4f3;
    --pink-soft: #fbdcf9;
    --ink: #111111;
  }
  * { margin: 0; padding: 0; box-sizing: border-box; }
  html, body { width: 1200px; height: 462px; overflow: hidden; background: var(--paper); }
  .card {
    position: relative;
    width: 1200px;
    height: 462px;
    background: var(--paper);
    font-family: "Arimo", Arial, sans-serif;
    color: var(--ink);
  }
  .card__field {
    position: absolute;
    left: 0; top: 60px;
    width: 1200px; height: 402px;
    background: var(--pink);
  }
  .brand-name {
    position: absolute;
    left: 220px; top: 118px;
    font-family: "Pinyon Script", cursive;
    font-size: 104px;
    line-height: 1;
    font-weight: 400;
    white-space: nowrap;
  }
  .brand-rule {
    position: absolute;
    left: 40px; top: 244px;
    width: 868px; height: 6px;
    background: var(--ink);
    border-radius: 3px;
  }
  .ornament {
    position: absolute;
    border-radius: 40% 10% 40% 10%;
    background: radial-gradient(ellipse at center, var(--ink) 0%, #3a2a38 45%, rgba(246,196,243,0) 75%);
  }
  .ornament--left { left: 27px; top: 182px; width: 200px; height: 130px; }
  .ornament--corner { left: 1018px; top: 300px; width: 156px; height: 108px; }
  .tagline {
    position: absolute;
    left: 227px; top: 252px;
    font-size: 47px;
    line-height: 1;
    white-space: nowrap;
  }
  .services {
    position: absolute;
    left: 917px; top: 77px;
    width: 259px; height: 283px;
    border: 5px solid var(--ink);
    background: var(--pink-soft);
    text-align: center;
    font-style: italic;
    font-size: 33px;
    line-height: 44px;
    padding-top: 12px;
  }
  .contact {
    position: absolute;
    left: 24px; top: 350px;
    font-size: 36px;
    line-height: 45px;
  }
  .contact__label { display: inline-block; width: 66px; }
  .abn {
    position: absolute;
    left: 927px; top: 420px;
    font-size: 24px;
    line-height: 1;
    white-space: nowrap;
  }
</style>
</head>
<body>
  <div class="card">
    <div class="card__field"></div>

    <div class="brand-name">Rosa Marindi</div>
    <div class="ornament ornament--left" role="img" aria-label="Black decorative flourish"></div>
    <div class="brand-rule"></div>
    <div class="tagline">Make up by Tessa Colwick</div>

    <div class="services">Bridal and<br>Special<br>Occasions<br>Make up</div>
    <div class="ornament ornament--corner" role="img" aria-label="Black decorative corner flourish"></div>

    <div class="contact">
      <div><span class="contact__label">Ph:</span>0412 385 604</div>
      <div><span class="contact__label">e:</span>rosamarindi@inboxly.net</div>
    </div>
    <div class="abn">ABN: 58204917362</div>
  </div>
</body>
</html>
```